'Tarvel' a financial/crypto-currency exchange in the middle east

On the card we need 1) Name 2) title 3) email address 4) phone number using the same colors and theme as the logo. On one side we just want the logo and we want the whole card to be in blue (same blue as logo) with the logo in the back being white.
Industry/Entity Type
Financial

```html
<!DOCTYPE html>
<html lang="en">
<head>
<meta charset="utf-8">
<title>Tarvel Business Card</title>
<link href="https://fonts.googleapis.com/css2?family=Jost:wght@400;700&family=Roboto:wght@400&display=swap" rel="stylesheet">
<style>
  :root {
    --brand-blue: #2577b5;
    --card-white: #f4f4f4;
    --ink-dark: #333333;
    --backdrop: #3b3b3b;
  }
  * { margin: 0; padding: 0; box-sizing: border-box; }
  html, body {
    width: 799px;
    height: 1200px;
    overflow: hidden;
    background: var(--backdrop);
  }
  .sheet {
    position: relative;
    width: 799px;
    height: 1200px;
  }
  .card {
    position: absolute;
    left: 80px;
    width: 640px;
    height: 366px;
    background: var(--card-white);
    border-radius: 26px;
    overflow: hidden;
  }
  .card--front { top: 117px; }
  .card--back { top: 717px; }

  .brand {
    display: flex;
    align-items: center;
    color: var(--brand-blue);
    font-family: "Jost", sans-serif;
    font-weight: 700;
    line-height: 1;
  }
  .brand__dot {
    border-radius: 50%;
    background: var(--brand-blue);
    flex: none;
  }
  .card--front .brand {
    position: absolute;
    left: 50%;
    top: 50%;
    transform: translate(-50%, -50%);
    gap: 18px;
    font-size: 64px;
  }
  .card--front .brand__dot { width: 84px; height: 84px; }

  .card--back .brand {
    position: absolute;
    left: 38px;
    top: 34px;
    gap: 12px;
    font-size: 34px;
  }
  .card--back .brand__dot { width: 48px; height: 48px; }

  .holder {
    position: absolute;
    left: 40px;
    top: 128px;
  }
  .holder__name {
    font-family: "Jost", sans-serif;
    font-weight: 700;
    font-size: 26px;
    color: var(--brand-blue);
    line-height: 1.1;
  }
  .holder__title {
    font-family: "Roboto", sans-serif;
    font-size: 14px;
    color: var(--ink-dark);
    margin-top: 2px;
  }
  .contacts {
    position: absolute;
    left: 40px;
    top: 208px;
    list-style: none;
    font-family: "Roboto", sans-serif;
    font-size: 16px;
    color: var(--ink-dark);
  }
  .contacts__item {
    display: flex;
    align-items: center;
    gap: 12px;
    height: 26px;
  }
  .contacts__icon { width: 14px; height: 14px; fill: var(--brand-blue); flex: none; }

  .backdrop-disc {
    position: absolute;
    left: 330px;
    top: 60px;
    width: 360px;
    height: 360px;
    border-radius: 50%;
    background: var(--brand-blue);
  }
</style>
</head>
<body>
<main class="sheet">
  <section class="card card--front">
    <div class="brand">
      <span class="brand__dot"></span>
      <span class="brand__name">Tarvel</span>
    </div>
  </section>

  <section class="card card--back">
    <div class="backdrop-disc"></div>
    <div class="brand">
      <span class="brand__dot"></span>
      <span class="brand__name">Tarvel</span>
    </div>
    <div class="holder">
      <p class="holder__name">Tarvel Smith</p>
      <p class="holder__title">Managing Director</p>
    </div>
    <ul class="contacts">
      <li class="contacts__item">
        <svg class="contacts__icon" viewBox="0 0 24 24" aria-hidden="true"><path d="M6.6 10.8a15.1 15.1 0 0 0 6.6 6.6l2.2-2.2c.3-.3.7-.4 1-.2 1.1.4 2.3.6 3.6.6.6 0 1 .4 1 1V20c0 .6-.4 1-1 1A17 17 0 0 1 3 4c0-.6.4-1 1-1h3.5c.6 0 1 .4 1 1 0 1.3.2 2.5.6 3.6.1.3 0 .7-.2 1z"/></svg>
        <span>555.555.5555</span>
      </li>
      <li class="contacts__item">
        <svg class="contacts__icon" viewBox="0 0 24 24" aria-hidden="true"><path d="M2 5h20v14H2z M3 6l9 7 9-7" fill="var(--brand-blue)"/><path d="M3 6l9 7 9-7" fill="none" stroke="#f4f4f4" stroke-width="1.5"/></svg>
        <span>tarvel@tarvelcrypto.com</span>
      </li>
      <li class="contacts__item">
        <svg class="contacts__icon" viewBox="0 0 24 24" aria-hidden="true"><circle cx="12" cy="12" r="10"/><path d="M2 12h20M12 2c3 3 3 17 0 20M12 2c-3 3-3 17 0 20" fill="none" stroke="#f4f4f4" stroke-width="1.4"/></svg>
        <span>www.tarvelcrypto.com</span>
      </li>
    </ul>
  </section>
</main>
</body>
</html>
```